Boutique custom software development company needs new business card

Our nearly 20 year old custom software development company would like to better include the fact that we are now providing Bitcoin services. These new services are B2B include education (how to acquire and securely hold Bitcoin) and integrating Bitcoin payments into existing ecommerce sites or other existing systems. Please keep the card clean and simple. Attached is our current design and some other files. vexalon.example

Target Market(s)

businesses owners interested in long term relationship

Industry/Entity Type

Custom software development and Bitcoin

Contact Information for Business Card

Marcus Ellwood, marcus@vexalon.example, vexalon.example, (888) 555-VEXAL

Font styles to use
Other font styles liked:
• monospace

Requirements
Must have
• double-sided
Nice to have
• clean and simple
Should not have
• physical address

```html
<!DOCTYPE html>
<html lang="en">
<head>
<meta charset="UTF-8">
<title>Vexalon Business Card</title>
<link href="https://fonts.googleapis.com/css2?family=Lato:wght@400&family=Open+Sans:wght@400;600;800&display=swap" rel="stylesheet">
<style>
  :root {
    --navy-deep: #0e2752;
    --navy-light: #3065a8;
    --brand-blue: #2f6db5;
    --brand-orange: #ec7a23;
    --ink: #3a3a3a;
    --paper: #ffffff;
    --paper-shade: #ececec;
    --backdrop: #dcdcdc;
  }
  * { margin: 0; padding: 0; box-sizing: border-box; }
  html, body {
    width: 1200px; height: 900px; overflow: hidden;
    background: var(--backdrop);
  }
  .sheet {
    position: relative; width: 1200px; height: 900px;
    display: flex; flex-direction: column; align-items: center;
    justify-content: center; gap: 40px;
  }
  .card {
    position: relative; width: 665px; height: 380px;
    box-shadow: 0 6px 18px rgba(0,0,0,0.25);
    overflow: hidden;
  }
  .card--front {
    background: radial-gradient(ellipse at 62% 58%, var(--navy-light) 0%, #1d4585 40%, var(--navy-deep) 85%);
  }
  .card--back {
    background: linear-gradient(105deg, var(--paper-shade) 0%, var(--paper) 55%, var(--paper) 100%);
  }
  .brand {
    position: absolute; right: 58px; text-align: left;
  }
  .card--front .brand { bottom: 70px; }
  .card--back .brand { top: 58px; }
  .brand__name {
    font-family: "Open Sans", sans-serif; font-weight: 800;
    font-size: 78px; line-height: 0.95; letter-spacing: 1px;
  }
  .brand__tagline {
    font-family: "Lato", sans-serif; font-weight: 400;
    font-size: 27px; letter-spacing: -0.3px; margin-top: 4px;
    padding-left: 40px;
  }
  .card--front .brand__name, .card--front .brand__tagline { color: var(--paper); }
  .card--back .brand__name, .card--back .brand__tagline { color: var(--brand-blue); }

  .identity {
    position: absolute; left: 56px; bottom: 96px;
    display: flex; align-items: baseline; gap: 10px;
    font-family: "Open Sans", sans-serif;
  }
  .identity__name {
    color: var(--brand-blue); font-weight: 600; font-size: 26px; letter-spacing: 0.5px;
  }
  .identity__divider { color: var(--brand-blue); font-size: 28px; font-weight: 400; }
  .identity__role { color: var(--ink); font-size: 15px; }

  .rule {
    position: absolute; left: 40px; right: 30px; bottom: 78px;
    height: 1px; background: var(--brand-orange);
  }
  .contacts {
    position: absolute; left: 56px; bottom: 42px;
    display: flex; align-items: center; gap: 10px;
    font-family: "Open Sans", sans-serif; font-size: 14.5px; color: var(--ink);
  }
  .contacts__item { display: flex; align-items: center; gap: 7px; }
  .contacts__icon { width: 16px; height: 16px; flex: none; }
  .contacts__sep { color: var(--brand-orange); font-size: 16px; }
</style>
</head>
<body>
<main class="sheet">
  <section class="card card--front" aria-label="Card front">
    <div class="brand">
      <div class="brand__name">VEXALON</div>
      <div class="brand__tagline">developer of custom applications</div>
    </div>
  </section>

  <section class="card card--back" aria-label="Card back">
    <div class="brand">
      <div class="brand__name">VEXALON</div>
      <div class="brand__tagline">developer of custom applications</div>
    </div>

    <div class="identity">
      <span class="identity__name">MARCUS ELLWOOD</span>
      <span class="identity__divider">|</span>
      <span class="identity__role">Bitcoin Educator</span>
    </div>

    <div class="rule"></div>

    <div class="contacts">
      <span class="contacts__item">
        <svg class="contacts__icon" viewBox="0 0 16 16" aria-hidden="true">
          <path d="M1 5c0-2 3-3 7-3s7 1 7 3v1h-3V4.5C11 4 10 3.8 8 3.8S5 4 4 4.5V6H1z" fill="var(--brand-blue)"/>
          <path d="M3 7h10l1 7H2z" fill="var(--brand-blue)"/>
          <circle cx="8" cy="10.5" r="1.8" fill="var(--paper)"/>
        </svg>
        (888) 555-VEXAL
      </span>
      <span class="contacts__sep">/</span>
      <span class="contacts__item">
        <svg class="contacts__icon" viewBox="0 0 16 16" aria-hidden="true">
          <rect x="1" y="4" width="14" height="10" rx="1" fill="var(--brand-blue)"/>
          <path d="M1.5 4.5 8 9.5l6.5-5" fill="none" stroke="var(--paper)" stroke-width="1.3"/>
        </svg>
        marcus@vexalon.example
      </span>
      <span class="contacts__sep">/</span>
      <span class="contacts__item">
        <svg class="contacts__icon" viewBox="0 0 16 16" aria-hidden="true">
          <circle cx="8" cy="8" r="6.5" fill="none" stroke="var(--brand-blue)" stroke-width="1.5"/>
          <ellipse cx="8" cy="8" rx="2.8" ry="6.5" fill="none" stroke="var(--brand-blue)" stroke-width="1.2"/>
          <path d="M1.5 8h13" stroke="var(--brand-blue)" stroke-width="1.2"/>
        </svg>
        www.vexalon.example
      </span>
    </div>
  </section>
</main>
</body>
</html>
```